Kelvor Plant Services

We are a heavy diesel mechanical business with additional air con certificates, remapping engine rebuilt

Contact Information for Business Card

Company Name, Director Name, Managing Director, Contact details, email and website

Font styles to use
Serif
Script

```html
<!DOCTYPE html>
<html lang="en">
<head>
<meta charset="utf-8">
<title>Kelvor Plant Services – Business Card</title>
<link rel="stylesheet" href="https://fonts.googleapis.com/css2?family=Noto+Serif:wght@400;700&display=swap">
<style>
  :root {
    --backdrop: #d6d6d6;
    --card-white: #f1f1f1;
    --navy: #1c1863;
    --navy-deep: #17145a;
    --ink: #111111;
    --white: #ffffff;
  }
  * { box-sizing: border-box; margin: 0; padding: 0; }
  html, body {
    width: 1200px; height: 1051px; overflow: hidden;
    background: var(--backdrop);
    font-family: "Noto Serif", Georgia, serif;
  }
  .canvas {
    position: relative; width: 1200px; height: 1051px;
    display: flex; flex-direction: column; align-items: center; justify-content: center; gap: 52px;
  }
  .card {
    position: relative; width: 760px; height: 434px; overflow: hidden;
    box-shadow: 0 10px 28px rgba(0,0,0,0.18);
  }

  /* Front */
  .card-front { background: var(--card-white); border-bottom: 4px solid var(--navy); }
  .front-brand {
    position: absolute; left: 52px; top: 40px;
    display: flex; align-items: center; gap: 14px;
  }
  .brand-dot {
    width: 26px; height: 26px; border-radius: 50%; background: var(--navy);
  }
  .brand-name {
    font-weight: 700; font-size: 30px; color: var(--navy); line-height: 1.1;
  }
  .contact-block { position: absolute; left: 52px; top: 128px; }
  .person {
    border-left: 10px solid var(--navy); padding-left: 14px; margin-bottom: 14px;
  }
  .person-name { font-weight: 700; font-size: 26px; letter-spacing: 0.5px; color: var(--navy); text-transform: uppercase; }
  .person-role { font-size: 18px; color: var(--navy); }
  .address { font-size: 18px; color: var(--ink); line-height: 1.4; margin-bottom: 10px; padding-left: 24px; }
  .contact-list { list-style: none; }
  .contact-list li {
    display: flex; align-items: center; gap: 10px;
    font-size: 18px; color: var(--ink); line-height: 1.5;
  }
  .contact-list svg { width: 14px; height: 14px; fill: var(--navy); flex: none; }
  .machine-art {
    position: absolute; left: 360px; top: 150px; width: 370px; height: 284px;
    background: linear-gradient(150deg, #2a2a2a 0%, #000000 70%);
    border-radius: 4px 4px 0 0;
  }

  /* Back */
  .card-back { background: var(--navy-deep); display: flex; align-items: center; justify-content: center; }
  .back-brand { display: flex; align-items: center; gap: 22px; }
  .back-brand .brand-dot { width: 40px; height: 40px; background: var(--white); }
  .back-brand .brand-name { color: var(--white); font-size: 50px; }
</style>
</head>
<body>
<main class="canvas">
  <section class="card card-front">
    <div class="front-brand">
      <span class="brand-dot"></span>
      <span class="brand-name">Kelvor Plant Services</span>
    </div>
    <div class="contact-block">
      <div class="person">
        <p class="person-name">Daniel Hart</p>
        <p class="person-role">Managing Director</p>
      </div>
      <p class="address">Your address, City<br>State, Zip 1234</p>
      <ul class="contact-list">
        <li><svg viewBox="0 0 24 24"><path d="M6.6 10.8a15 15 0 0 0 6.6 6.6l2.2-2.2a1 1 0 0 1 1-.25 11.4 11.4 0 0 0 3.6.57 1 1 0 0 1 1 1V20a1 1 0 0 1-1 1A17 17 0 0 1 3 4a1 1 0 0 1 1-1h3.5a1 1 0 0 1 1 1c0 1.25.2 2.45.57 3.57a1 1 0 0 1-.25 1z"/></svg>123 456 789</li>
        <li><svg viewBox="0 0 24 24"><path d="M2 5h20v14H2zm2 2v.5l8 5 8-5V7l-8 5z"/></svg>info@yourgmail.com</li>
        <li><svg viewBox="0 0 24 24"><path d="M12 2a10 10 0 1 0 0 20 10 10 0 0 0 0-20zm0 2c1 0 2.3 2 2.8 5H9.2C9.7 6 11 4 12 4zM4.3 11h4.6a18 18 0 0 0 0 2H4.3a8 8 0 0 1 0-2zm10.8 0h4.6a8 8 0 0 1 0 2h-4.6a18 18 0 0 0 0-2zM9.2 15h5.6c-.5 3-1.8 5-2.8 5s-2.3-2-2.8-5z"/></svg>www.yourwebsite.com</li>
      </ul>
    </div>
    <div class="machine-art" role="img" aria-label="Black silhouette of an excavator boom and bucket"></div>
  </section>

  <section class="card card-back">
    <div class="back-brand">
      <span class="brand-dot"></span>
      <span class="brand-name">Kelvor Plant Services</span>
    </div>
  </section>
</main>
</body>
</html>
```